Automotive dealership needs a brochure for innovative vehicle locate service

Pairing buyers with the best solution for their vehicle needs is what we do. When we don't have that perfect vehicle in-stock, we will put our expertise and resources to work finding it. This brochure will be used in presenting our buying service to customers. The color and font scheme needs to align with our branding guide in the examples. A sample brochure for what we need has been included as well as some other branded company materials for reference.
Target Market(s)
Middle-income buyers. These people are buying vehicles that will be their daily driver to work and activities.
Industry/Entity Type
Automotive Retail
Requirements
Must have
- Refer to the branding guide.
Nice to have
- A friendly, welcoming, approachable feel that shows crisp and capable professionalism.
Should not have
- Colors that do not match our branding guide. Exotic or high-end vehicle/buyer imagery.

```html
<!DOCTYPE html>
<html lang="en">
<head>
<meta charset="utf-8">
<title>Harlow Motors – Buying Service Brochure</title>
<link rel="stylesheet" href="https://fonts.googleapis.com/css2?family=Montserrat:wght@500;700;800;900&family=Open+Sans:wght@400;600&display=swap">
<style>
  :root {
    --ink: #101010;
    --charcoal: #1c1c1e;
    --graphite: #2a2a2d;
    --yellow: #f5b800;
    --yellow-deep: #d99e00;
    --white: #ffffff;
    --muted: #c9c9c9;
    --page-bg: #dcdcdc;
  }
  * { box-sizing: border-box; margin: 0; padding: 0; }
  html, body { width: 900px; height: 1200px; overflow: hidden; background: var(--page-bg); }
  body { font-family: "Open Sans", Arial, sans-serif; color: var(--white); }

  .canvas { position: relative; width: 900px; height: 1200px; }

  .spread {
    position: absolute; left: 20px; width: 860px; height: 540px;
    display: grid; grid-template-columns: repeat(3, 1fr);
    background: var(--ink);
    box-shadow: 0 6px 18px rgba(0,0,0,.25);
    overflow: hidden;
  }
  .spread--outside { top: 30px; }
  .spread--inside { top: 630px; }

  .panel { position: relative; overflow: hidden; border-right: 1px solid rgba(255,255,255,.06); }
  .panel:last-child { border-right: none; }

  .photo { position: absolute; }

  /* brand mark */
  .brand { display: flex; align-items: center; gap: 7px; }
  .brand__square { width: 14px; height: 14px; background: var(--yellow); }
  .brand__name {
    font-family: "Montserrat", Arial, sans-serif; font-weight: 800;
    font-size: 15px; letter-spacing: 1px; color: var(--white);
  }

  .heading {
    font-family: "Montserrat", Arial, sans-serif; font-weight: 800;
    font-size: 11px; letter-spacing: .6px; color: var(--yellow); text-transform: uppercase;
    margin-bottom: 5px;
  }
  .heading--bar {
    display: inline-block; background: var(--yellow); color: var(--ink);
    padding: 3px 8px;
  }
  .body-text { font-size: 9px; line-height: 1.5; color: var(--muted); margin-bottom: 12px; }

  /* outside: back panel */
  .back { background: var(--charcoal); padding: 22px 20px; }
  .back .brand { margin-bottom: 18px; }
  .back__rule { height: 4px; width: 60px; background: var(--yellow); margin-bottom: 18px; }
  .back__skyline {
    left: 0; right: 0; bottom: 0; height: 170px;
    background: linear-gradient(180deg, #8fa3b8 0%, #5a6b7d 55%, #2b3440 100%);
  }
  .back__stripe { position: absolute; left: 0; bottom: 0; width: 100%; height: 170px; }

  /* outside: middle panel */
  .promo { background: var(--ink); }
  .promo__truck {
    left: 0; right: 0; bottom: 0; height: 210px;
    background: linear-gradient(160deg, #6f7f92 0%, #3a3f48 50%, #141414 100%);
  }
  .promo__badge {
    position: absolute; top: 40px; left: 24px; width: 180px; height: 180px;
    border-radius: 50%; background: var(--yellow);
    display: flex; flex-direction: column; justify-content: center; align-items: center;
    text-align: center; color: var(--ink);
    font-family: "Montserrat", Arial, sans-serif;
  }
  .promo__small { font-size: 11px; font-weight: 700; letter-spacing: 1px; }
  .promo__big { font-size: 26px; font-weight: 900; line-height: 1; margin: 3px 0; }
  .contact { position: absolute; left: 24px; top: 245px; right: 20px; }
  .contact__row { display: flex; align-items: center; gap: 8px; font-size: 10px; margin-bottom: 9px; color: var(--white); }
  .contact__icon { width: 20px; height: 20px; border-radius: 50%; background: var(--yellow); display: flex; align-items: center; justify-content: center; flex: none; }

  /* outside: cover */
  .cover { background: var(--ink); }
  .cover .brand { position: absolute; top: 22px; left: 22px; z-index: 2; }
  .cover__tilt { position: absolute; left: 0; top: 0; width: 100%; height: 100%; z-index: 1; }
  .cover__title {
    position: absolute; top: 100px; right: 22px; text-align: right; z-index: 2;
    font-family: "Montserrat", Arial, sans-serif; font-weight: 900; line-height: 1;
  }
  .cover__title-top { font-size: 36px; color: var(--yellow); display: block; }
  .cover__title-bottom { font-size: 36px; color: var(--white); display: block; }
  .cover__tagline { position: absolute; top: 186px; right: 22px; font-size: 9px; color: var(--muted); z-index: 2; }
  .cover__cars {
    left: 0; right: 0; bottom: 0; height: 230px;
    background: linear-gradient(170deg, #9fb2c6 0%, #b43a32 55%, #2a2a2a 100%);
  }

  /* inside: left */
  .guide { background: var(--charcoal); }
  .guide__handshake {
    left: 0; right: 0; top: 0; height: 175px;
    background: linear-gradient(135deg, #54585f 0%, #2c2e33 60%, #151515 100%);
  }
  .guide__content { position: absolute; top: 195px; left: 20px; right: 20px; }

  /* inside: middle */
  .steps { background: var(--ink); padding: 24px 20px; }
  .step { display: flex; gap: 10px; margin-bottom: 20px; }
  .step__num {
    flex: none; width: 26px; height: 26px; border-radius: 50%;
    background: var(--yellow); color: var(--ink);
    font-family: "Montserrat", Arial, sans-serif; font-weight: 800; font-size: 12px;
    display: flex; align-items: center; justify-content: center;
  }
  .step .body-text { margin-bottom: 0; }
  .steps .brand { position: absolute; left: 20px; bottom: 26px; }
  .steps__web { position: absolute; left: 20px; bottom: 10px; font-size: 8px; color: var(--muted); }

  /* inside: right */
  .benefits { background: var(--charcoal); }
  .benefits__lot {
    left: 0; right: 0; top: 0; height: 170px;
    background: linear-gradient(180deg, #d4d8dc 0%, #9aa1a8 60%, #5d636a 100%);
  }
  .benefits__content { position: absolute; top: 188px; left: 20px; right: 20px; }
  .benefits__band { position: absolute; left: 0; bottom: 0; width: 100%; height: 190px; }
  .benefits__car {
    left: 0; right: 0; bottom: 0; height: 150px;
    background: linear-gradient(160deg, #f5c53a 0%, #d99e00 45%, #3a3a3a 100%);
  }
</style>
</head>
<body>
<div class="canvas">

  <section class="spread spread--outside">
    <article class="panel back">
      <div class="brand"><span class="brand__square"></span><span class="brand__name">HARLOW MOTORS</span></div>
      <div class="back__rule"></div>
      <h3 class="heading">Who We Are</h3>
      <p class="body-text">We pair everyday drivers with the right vehicle, and when it is not on our lot, we find it for you.</p>
      <h3 class="heading">Our Promise</h3>
      <p class="body-text">Honest pricing, clear updates and a team that works for you from search to keys.</p>
      <div class="photo back__skyline" role="img" aria-label="City skyline at dusk"></div>
      <svg class="back__stripe" viewBox="0 0 287 170" preserveAspectRatio="none">
        <polygon points="0,0 120,0 60,170 0,170" fill="var(--yellow)" opacity=".9"/>
      </svg>
    </article>

    <article class="panel promo">
      <div class="promo__badge">
        <span class="promo__small">YOUR NEXT</span>
        <span class="promo__big">VEHICLE</span>
        <span class="promo__small">IS JUST A CALL AWAY</span>
      </div>
      <div class="contact">
        <div class="contact__row">
          <span class="contact__icon"><svg width="10" height="10" viewBox="0 0 24 24"><path fill="#101010" d="M6.6 10.8a15 15 0 0 0 6.6 6.6l2.2-2.2a1 1 0 0 1 1-.25 11.4 11.4 0 0 0 3.6.6 1 1 0 0 1 1 1V20a1 1 0 0 1-1 1A17 17 0 0 1 3 4a1 1 0 0 1 1-1h3.5a1 1 0 0 1 1 1c0 1.25.2 2.45.6 3.6a1 1 0 0 1-.25 1z"/></svg></span>
          555-014-2200
        </div>
        <div class="contact__row">
          <span class="contact__icon"><svg width="10" height="10" viewBox="0 0 24 24"><circle cx="12" cy="12" r="9" fill="none" stroke="#101010" stroke-width="2.5"/><path d="M3 12h18M12 3c3 3 3 15 0 18M12 3c-3 3-3 15 0 18" fill="none" stroke="#101010" stroke-width="2"/></svg></span>
          harlowmotors.example
        </div>
        <div class="contact__row">
          <span class="contact__icon"><svg width="10" height="10" viewBox="0 0 24 24"><path fill="#101010" d="M12 2a7 7 0 0 0-7 7c0 5 7 13 7 13s7-8 7-13a7 7 0 0 0-7-7zm0 9.5A2.5 2.5 0 1 1 12 6.5a2.5 2.5 0 0 1 0 5z"/></svg></span>
          1200 Harlow Way, Omaha
        </div>
      </div>
      <div class="photo promo__truck" role="img" aria-label="Dark pickup truck parked in front of a city skyline"></div>
    </article>

    <article class="panel cover">
      <svg class="cover__tilt" viewBox="0 0 287 540" preserveAspectRatio="none">
        <polygon points="287,222 287,258 0,312 0,276" fill="var(--yellow)"/>
      </svg>
      <div class="brand"><span class="brand__square"></span><span class="brand__name">HARLOW MOTORS</span></div>
      <h1 class="cover__title">
        <span class="cover__title-top">BUYING</span>
        <span class="cover__title-bottom">SERVICE</span>
      </h1>
      <p class="cover__tagline">We find the car. You enjoy the drive.</p>
      <div class="photo cover__cars" role="img" aria-label="Red pickup truck and dark SUV in front of city buildings"></div>
    </article>
  </section>

  <section class="spread spread--inside">
    <article class="panel guide">
      <div class="photo guide__handshake" role="img" aria-label="Salesperson handing car keys to a buyer"></div>
      <div class="guide__content">
        <h3 class="heading heading--bar">How Does It Work?</h3>
        <p class="body-text">Tell us the make, model, budget and features you need. Our buyers search trusted auctions and partner dealers nationwide.</p>
        <h3 class="heading heading--bar">What Does It Cost?</h3>
        <p class="body-text">One simple flat fee, shared up front, with no surprises at signing.</p>
      </div>
    </article>

    <article class="panel steps">
      <div class="step"><span class="step__num">1</span><div><h3 class="heading">Share Your List</h3><p class="body-text">Tell us the vehicle, colour and budget that fit your life.</p></div></div>
      <div class="step"><span class="step__num">2</span><div><h3 class="heading">We Start Searching</h3><p class="body-text">Our team checks hundreds of sources to find your best match.</p></div></div>
      <div class="step"><span class="step__num">3</span><div><h3 class="heading">Review Your Options</h3><p class="body-text">We send photos, history and pricing so you choose with confidence.</p></div></div>
      <div class="step"><span class="step__num">4</span><div><h3 class="heading">Drive It Home</h3><p class="body-text">We inspect, prepare and deliver the vehicle ready for the road.</p></div></div>
      <div class="brand"><span class="brand__square"></span><span class="brand__name">HARLOW MOTORS</span></div>
      <p class="steps__web">harlowmotors.example</p>
    </article>

    <article class="panel benefits">
      <div class="photo benefits__lot" role="img" aria-label="Row of vehicles on a dealership lot"></div>
      <div class="benefits__content">
        <h3 class="heading heading--bar">Why Use Our Service?</h3>
        <p class="body-text">Save hours of searching and get a vehicle checked by our own technicians.</p>
      </div>
      <svg class="benefits__band" viewBox="0 0 287 190" preserveAspectRatio="none">
        <polygon points="0,60 287,0 287,40 0,100" fill="var(--yellow)"/>
      </svg>
      <div class="photo benefits__car" role="img" aria-label="Yellow compact car"></div>
    </article>
  </section>

</div>
</body>
</html>
```